Vocational Mentor needs an impressive business card

1. I need a business card (or maybe three with identic look) to promote me and my three business titles/services:
- Vocational Mentor. I help people find their vocation and live happily from it. I use my 20 years of experience in business, management and psychology to help them identify the most efficient ways to make a living doing what they are passionate about.
- Business Angel. I help founders start a succesful business with minimum risks and costs. I use my 20 years of experience in sales, management and entrepreneurship to help them identify the most efficient ways, in terms of time and cost, to validate their business idea.
- Learning Designer. I design unique learning programs that produce long-term cognitive and behavioural changes to people and organisations. I use my 20 years of experience in learning, teaching and change management to create minimalist experiences and processes that allow them to change efficiently in their pursued direction.

2. I would like a two-sided business card, on the front with my name, contact details and titles, on the back the explanation of the services.
Updates

Hi all,

I updated my brief, included contacts info and give feedback on all designs I got. I am new on this platform so please tell me if you need anything else or if I don't use corectly the platform forms.

Kind regards,
Mirel

Hi all,

I shortened the services description by deleting the phrase "I call..."

Kind regards,
Mirel

Target Market(s)

Freelancers, startups, people and organization willing to invest in change through ultimate learning experiences

Industry/Entity Type

Business

Font styles to use
Serif

Requirements
Must have
• Front side: full name, titles, web site, email, phone like below:
Mirel Vantaru
Vocational Mentor, Business Angel, Learning Designer
info@mirelvantaru.example
www.mirelvantaru.example
+40-748-MIRELV
Nice to have
• Back side: the description of the services I provide as in the task description.
1/3: it would be nice if I can jam all three titles on the front side but then I need a solution to jam all three services on the back side.

```html
<!DOCTYPE html>
<html lang="en">
<head>
<meta charset="utf-8">
<title>Mirel Vantaru – Business Card</title>
<link rel="stylesheet" href="https://fonts.googleapis.com/css2?family=Source+Serif+4:opsz,wght@8..60,400;8..60,600;8..60,700&display=swap">
<style>
  :root {
    --card-red: #a50b1f;
    --card-cream: #e5e1d2;
    --ink-cream: #f3e9dc;
    --ink-red: #a50b1f;
    --backdrop: #ecebe8;
  }
  * { margin: 0; padding: 0; box-sizing: border-box; }
  html, body { width: 1200px; height: 900px; overflow: hidden; }
  body {
    position: relative;
    background: var(--backdrop);
    font-family: "Source Serif 4", Georgia, serif;
  }
  .card {
    position: absolute;
    top: 136px;
    width: 360px;
    height: 628px;
    box-shadow: 0 2px 6px rgba(0,0,0,0.12);
  }
  .card-front { left: 214px; background: var(--card-cream); }
  .card-back  { left: 626px; background: var(--card-red); color: var(--ink-cream); }

  .front-band {
    position: absolute; left: 0; top: 0;
    width: 100%; height: 234px;
    background: var(--card-red);
  }
  .holder-name {
    position: absolute; left: 34px; top: 124px;
    font-size: 40px; font-weight: 400; line-height: 42px;
    color: var(--ink-cream);
    letter-spacing: -0.5px;
  }
  .title-list {
    position: absolute; left: 34px; top: 252px;
    list-style: none;
    font-size: 15.5px; font-weight: 700; line-height: 24.5px;
    letter-spacing: 1px; text-transform: uppercase;
    color: var(--ink-red);
  }
  .contact-list {
    position: absolute; left: 34px; top: 522px;
    list-style: none;
    font-size: 20px; line-height: 25.5px;
    color: var(--ink-red);
  }

  .service {
    position: absolute; left: 0; width: 100%;
    text-align: center;
  }
  .service-1 { top: 51px; }
  .service-2 { top: 210px; }
  .service-3 { top: 388px; }
  .service-title {
    font-size: 15.5px; font-weight: 700; letter-spacing: 1px;
    text-transform: uppercase; line-height: 20px;
    margin-bottom: 6px;
  }
  .service-text {
    font-size: 14.6px; line-height: 18.2px;
  }
</style>
</head>
<body>
  <section class="card card-front" aria-label="Business card front">
    <div class="front-band"></div>
    <h1 class="holder-name">Mirel<br>Vantaru</h1>
    <ul class="title-list">
      <li>Vocational Mentor</li>
      <li>Business Angel</li>
      <li>Learning Designer</li>
    </ul>
    <ul class="contact-list">
      <li>+40-748-MIRELV</li>
      <li>info@mirelvantaru.example</li>
      <li>www.mirelvantaru.example</li>
    </ul>
  </section>

  <section class="card card-back" aria-label="Business card back">
    <div class="service service-1">
      <h2 class="service-title">Vocational Mentor</h2>
      <p class="service-text">I help people to find their vocation and<br>live happily from it. I use my 20 years<br>of experience in business, management<br>and psychology to help them identify<br>the most efficient ways to make a living<br>doing what they are passionate about.</p>
    </div>
    <div class="service service-2">
      <h2 class="service-title">Business Angel</h2>
      <p class="service-text">I help founders to start a succesful<br>business with minimum risks and costs.<br>I use my 20 years of experience in sales,<br>management and entrepreneurship to<br>help them identify the most efficient<br>ways, in terms of time and cost, to<br>validate their business idea.</p>
    </div>
    <div class="service service-3">
      <h2 class="service-title">Learning Designer</h2>
      <p class="service-text">I design unique learning programs<br>that produce long-term cognitive and<br>behavioural changes to people and<br>organisations. I use my 20 years of<br>experience in learning, teaching and<br>change management to create minimalist<br>experiences and processes that allows<br>them to change efficiently in their<br>pursued direction.</p>
    </div>
  </section>
</body>
</html>
```